Watch brand needs new business cards

Kestrel Timepiece Company are looking for a new business card design incorporating our logo and brand colours as per our website.

Design should be 90x55mm with 3mm print margin from edges and 3mm external bleed.

Card should be double sided, e.g. logo one side, personal details on the other.

Logo will be provided as a vector.

The card must be able to show:
- Staff name
- Position
- Office Address
- Email
- Telephone number
- Website address

Final work must be provided in an editable format to allow us to add staff details (e.g. an AI or PSD file).

```html
<!DOCTYPE html>
<html lang="en">
<head>
<meta charset="utf-8">
<title>Kestrel Timepiece Company – Business Card</title>
<link rel="stylesheet" href="https://fonts.googleapis.com/css2?family=Open+Sans:wght@400&family=Tinos:wght@400;700&display=swap">
<style>
  :root {
    --backdrop: #d8d5d2;
    --card-light: #f3f2f1;
    --card-dark: #1b1919;
    --ink: #111010;
    --ink-soft: #2a2828;
    --paper: #ffffff;
  }
  * { margin: 0; padding: 0; box-sizing: border-box; }
  html, body {
    width: 1200px;
    height: 900px;
    overflow: hidden;
    background: var(--backdrop);
  }
  .business-card {
    position: absolute;
    left: 150px;
    top: 175px;
    width: 900px;
    height: 550px;
    border-radius: 26px;
    overflow: hidden;
    background: var(--card-light);
    box-shadow: 0 10px 30px rgba(0,0,0,0.18);
  }
  .feature-panel {
    position: absolute;
    inset: 0;
    width: 900px;
    height: 550px;
  }
  .brand {
    position: absolute;
    left: 60px;
    top: 38px;
    width: 350px;
    text-align: center;
    color: var(--ink);
    font-family: "Tinos", "Times New Roman", serif;
    font-weight: 700;
  }
  .brand-dot {
    display: block;
    width: 88px;
    height: 88px;
    margin: 0 auto 24px;
    border-radius: 50%;
    border: 4px solid var(--ink);
  }
  .brand-name {
    display: block;
    font-size: 42px;
    letter-spacing: 2px;
    line-height: 1;
    text-transform: uppercase;
  }
  .brand-tagline {
    display: block;
    margin-top: 8px;
    font-size: 16px;
    letter-spacing: 3.5px;
    text-transform: uppercase;
  }
  .staff {
    position: absolute;
    left: 42px;
    top: 328px;
    color: var(--ink);
  }
  .staff-name {
    font-family: "Tinos", "Times New Roman", serif;
    font-weight: 700;
    font-size: 36px;
    line-height: 1.1;
  }
  .staff-role {
    font-family: "Open Sans", Arial, sans-serif;
    font-size: 21px;
    color: var(--ink-soft);
    margin-top: 2px;
  }
  .office-address {
    margin-top: 40px;
    margin-left: 6px;
    font-family: "Open Sans", Arial, sans-serif;
    font-style: normal;
    font-size: 22px;
    line-height: 1.5;
    color: var(--ink-soft);
  }
  .contact-list {
    position: absolute;
    right: 48px;
    top: 218px;
    list-style: none;
    text-align: right;
    font-family: "Open Sans", Arial, sans-serif;
    font-size: 22px;
    line-height: 34px;
    color: var(--paper);
  }
  .contact-list li {
    display: flex;
    justify-content: flex-end;
    align-items: center;
    gap: 10px;
  }
  .contact-icon {
    width: 17px;
    height: 17px;
    fill: var(--paper);
    flex: none;
  }
</style>
</head>
<body>
  <article class="business-card">
    <svg class="feature-panel" viewBox="0 0 900 550" role="img" aria-label="Clock hands graphic area">
      <path d="M655 0 L900 0 L900 550 L690 550 L470 262 Z" fill="var(--card-dark)"/>
    </svg>

    <div class="brand">
      <span class="brand-dot"></span>
      <span class="brand-name">Kestrel</span>
      <span class="brand-tagline">Timepiece Company</span>
    </div>

    <div class="staff">
      <h1 class="staff-name">Daniel Hartley</h1>
      <p class="staff-role">Managing Director</p>
      <address class="office-address">
        12345, Address Goes Here<br>
        Country Name, 123456.
      </address>
    </div>

    <ul class="contact-list">
      <li>044-555 018 732
        <svg class="contact-icon" viewBox="0 0 20 20"><path d="M2 8 C2 4 6 3 10 3 C14 3 18 4 18 8 L14 9 L13 6.5 C11 6 9 6 7 6.5 L6 9 Z M5 11 L15 11 L17 17 L3 17 Z"/></svg>
      </li>
      <li>info@kestreltime.com
        <svg class="contact-icon" viewBox="0 0 20 20"><path d="M2 4 H18 V16 H2 Z"/><path d="M2 4 L10 11 L18 4" fill="none" stroke="#1b1919" stroke-width="1.6"/></svg>
      </li>
      <li>www.kestreltime.com
        <svg class="contact-icon" viewBox="0 0 20 20"><g fill="none" stroke="#fff" stroke-width="2.2" stroke-linecap="round"><path d="M8.5 11.5 L11.5 8.5"/><path d="M9 6 L11.5 3.5 A3 3 0 0 1 16.5 8.5 L14 11"/><path d="M11 14 L8.5 16.5 A3 3 0 0 1 3.5 11.5 L6 9"/></g></svg>
      </li>
    </ul>
  </article>
</body>
</html>
```